Voltarra: Electrical Contractor flyer design.

We are looking for a sharp and professional flyer to promote the business's cost for specific jobs and to promote the business.
We are a small electrical business looking to break into the market.
Attached logo to be used and following content to be incorporated. Contact details will be given upon final flyer design.

Internal Power Points: $ 120
External Weather Proof Power Points: $150
T.V. Points: $120 (excludes aerial)
T.V. Mounting: $ 200 (Exclude Leads)
Aerials Starting From: $220 Incudes Mast
LED Down lights: $60 per unti
Ceiling Fans: $150 (Fan Excluded)
Oven & Range Hood Change Overs: $250
A.C. Install: $300
S/B Upgrade: From $600
Safety Switch Installation: $280
Phone Points: $120

Services Incude:

New home wiring
Shop & Office Fit Outs
Re - Wires
Extentions
Garden Lighting
Home Thearters
Home Automation
Power Points
Phone, Data
Feature Lighting
Lighting design and Installation
Ceiling Fans
A.C Installation
Oven & Range hood Installation

*All prices are gst inclusive
**Prices subject to change due to site access.

```html
<!DOCTYPE html>
<html lang="en">
<head>
<meta charset="utf-8">
<title>Voltarra — Electricity in Motion</title>
<link href="https://fonts.googleapis.com/css2?family=Audiowide&family=Arimo:wght@400;700&display=swap" rel="stylesheet">
<style>
  :root {
    --orange: #e8661e;
    --orange-light: #f79a1e;
    --orange-deep: #c9470f;
    --price: #e2661c;
    --ink: #4d4d4f;
    --rule: #6b6b6d;
    --paper: #ffffff;
  }
  html, body { margin: 0; padding: 0; overflow: hidden; background: var(--paper); }
  .flyer {
    position: relative;
    width: 846px;
    height: 1200px;
    overflow: hidden;
    background: var(--paper);
    font-family: "Arimo", Arial, sans-serif;
  }
  .hero {
    position: absolute; left: 0; top: 0;
    width: 846px; height: 456px;
    background: radial-gradient(circle at 10% 55%, #ffd66a 0%, var(--orange-light) 22%, var(--orange) 60%, var(--orange-deep) 100%);
  }
  .tab { position: absolute; left: 0; top: 0; }
  .headline {
    position: absolute; left: 0; width: 846px; top: 400px;
    text-align: center;
    font-family: "Audiowide", sans-serif;
    color: var(--ink);
    font-size: 34px;
    line-height: 48px;
    letter-spacing: 5px;
    text-transform: uppercase;
  }
  .tagline {
    position: absolute; left: 68px; width: 710px; top: 510px; height: 55px;
    border-top: 2px solid var(--rule);
    border-bottom: 2px solid var(--rule);
    box-sizing: border-box;
    text-align: center;
    font-family: "Audiowide", sans-serif;
    font-size: 47px;
    line-height: 51px;
    letter-spacing: 4px;
    color: var(--orange);
    text-transform: uppercase;
  }
  .tagline span { display: inline-block; transform: skewX(-14deg); }
  .price-list {
    position: absolute; left: 0; width: 846px; top: 603px;
    margin: 0; padding: 0; list-style: none;
    text-align: center;
    font-size: 22.5px;
    line-height: 32.3px;
  }
  .price-list .job { font-weight: 700; color: var(--ink); }
  .price-list .cost { color: var(--price); }
  .footer-band { position: absolute; left: 0; top: 1020px; }
  .brand {
    position: absolute; left: 0; width: 846px; top: 1080px;
    display: flex; justify-content: center; align-items: center; gap: 14px;
    font-family: "Arimo", Arial, sans-serif;
    font-weight: 700;
    font-size: 60px;
    color: var(--ink);
  }
  .brand-mark { width: 22px; height: 22px; background: var(--ink); }
</style>
</head>
<body>
<div class="flyer">
  <div class="hero" role="img" aria-label="Photograph of a row of hanging orange light bulbs with one glowing white bulb swinging to the left, on an orange background"></div>

  <svg class="tab" width="846" height="460" viewBox="0 0 846 460" aria-hidden="true">
    <path d="M164 457 L176 393 Q179 378 195 378 L672 378 Q690 378 687 393 L676 457 Z" fill="var(--paper)"/>
  </svg>

  <h1 class="headline" style="margin:0">Electricity<br>in Motion</h1>

  <div class="tagline"><span>At Best Prices</span></div>

  <ul class="price-list">
    <li><span class="job">Internal Power Points:</span> <span class="cost">$120</span></li>
    <li><span class="job">External Weather Proof Power Points:</span> <span class="cost">$150</span></li>
    <li><span class="job">T.V. Points:</span> <span class="cost">$120 (excludes aerial)</span></li>
    <li><span class="job">T.V. Mounting:</span> <span class="cost">$200 (Exclude Leads)</span></li>
    <li><span class="job">Aerials Starting From:</span> <span class="cost">$220 Incudes Mast</span></li>
    <li><span class="job">LED Down lights:</span> <span class="cost">$60 per unti</span></li>
    <li><span class="job">Ceiling Fans:</span> <span class="cost">$150 (Fan Excluded)</span></li>
    <li><span class="job">Oven &amp; Range Hood Change Overs:</span> <span class="cost">$250</span></li>
    <li><span class="job">A.C. Install:</span> <span class="cost">$300</span></li>
    <li><span class="job">S/B Upgrade:</span> <span class="cost">from $600</span></li>
    <li><span class="job">Safety Switch Installation:</span> <span class="cost">$280</span></li>
    <li><span class="job">Phone Points:</span> <span class="cost">$120</span></li>
  </ul>

  <svg class="footer-band" width="846" height="180" viewBox="0 0 846 180" aria-hidden="true">
    <defs>
      <linearGradient id="bandFill" x1="0" y1="0" x2="1" y2="1">
        <stop offset="0" stop-color="#e9641c"/>
        <stop offset="1" stop-color="#f0802a"/>
      </linearGradient>
    </defs>
    <polygon points="0,0 176,0 136,180 0,180" fill="url(#bandFill)"/>
    <polygon points="686,0 846,0 846,180 646,180" fill="url(#bandFill)"/>
  </svg>

  <div class="brand"><span class="brand-mark"></span><span>Voltarra</span></div>
</div>
</body>
</html>
```